IT Professional Services Marketing Web Site

The Kovrel Associates new web site, need to look clean and modern, it has to give the feel of a professional IT consulting firm (something like white / clean background), the design need to be influenced by this site: http://www.trundavio.com/ .
The whole site is a one page, plus a link to a blog site, with the following sections:
1. Menu
2. Main Area
3. Our Company
4. What we do
5. Our Clients
6. Our People
7. Events
8. Contact Us
The new web site will be hosted on WordPress
Updates

Target Market(s)

Project Management Offices in Medium to Large Organisations

Industry/Entity Type

It Company

Number of Pages Required

1 page

Font styles to use
Serif
Sans Serif

Requirements
Must have
• Implemented on WordPress
Nice to have
• Shadows on the images and areas to give the site a bit of depth

```html
<!DOCTYPE html>
<html lang="en">
<head>
<meta charset="utf-8">
<title>Kovrel Associates — Trusted PMO Partners</title>
<link href="https://fonts.googleapis.com/css2?family=Raleway:wght@300;400;600;700&family=Open+Sans:wght@400;600;700&display=swap" rel="stylesheet">
<style>
:root{
  --orange:#f7931e;
  --blue:#29a9e1;
  --blue-soft:#5fbfe9;
  --ink:#333333;
  --muted:#6d6d6d;
  --light:#f4f4f4;
  --band:#e9e9ea;
  --charcoal:#3b3b3d;
  --charcoal-dark:#2c2c2e;
  --white:#ffffff;
  --lavender:#e9e6f2;
}
*{box-sizing:border-box;margin:0;padding:0}
html,body{width:1200px;height:5000px;overflow:hidden}
body{font-family:"Open Sans",Arial,sans-serif;color:var(--ink);background:var(--white);font-size:14px;line-height:1.6}
h1,h2,h3,h4{font-family:"Raleway",Helvetica,sans-serif}
.ph{display:block}

/* header */
.site-header{height:80px;display:flex;align-items:center;justify-content:space-between;padding:0 80px;background:var(--white);box-shadow:0 2px 6px rgba(0,0,0,.08);position:relative;z-index:2}
.brand{font-family:"Raleway",sans-serif;font-weight:600;font-size:24px;color:var(--ink)}
.main-nav{display:flex;gap:6px}
.main-nav a{font-family:"Raleway",sans-serif;font-size:14px;color:var(--ink);text-decoration:none;padding:6px 12px;border-right:1px solid #ddd}
.main-nav a:last-child{border-right:0}

/* hero */
.hero{height:500px;background:linear-gradient(180deg,#f3f1f8 0%,var(--lavender) 70%,#d9d4e8 100%);display:flex;align-items:center;justify-content:space-between;padding:0 80px}
.hero-copy h1{font-size:34px;font-weight:700;color:var(--ink);margin-bottom:10px}
.hero-copy p{font-family:"Raleway",sans-serif;font-size:20px;color:var(--ink);line-height:1.4}
.hero-art{width:540px;height:380px;border-radius:6px;background:radial-gradient(circle at 50% 50%,#c9c6dc 0%,#dcd8ea 60%,rgba(233,230,242,0) 100%)}

/* intro */
.intro{height:420px;padding-top:70px}
.intro p{font-size:13.5px;color:var(--muted);margin-bottom:16px;width:920px;margin-left:auto;margin-right:auto}
.intro strong{color:var(--ink)}

/* services timeline */
.services{height:880px;background:var(--band);position:relative;padding-top:40px}
.services::before{content:"";position:absolute;left:599px;top:40px;bottom:40px;width:2px;background:#c9c9c9}
.service{height:266px;position:relative}
.service-left,.service-right{position:absolute;top:50%;transform:translateY(-50%);width:400px}
.service-left{left:120px}
.service-right{left:680px}
.service-text{font-size:13px;color:var(--muted)}
.service-left.service-text{text-align:right}
.service-node{position:absolute;left:559px;top:50%;transform:translateY(-50%);width:82px;height:82px;border-radius:50%;background:var(--orange);border:5px solid var(--white);box-shadow:0 2px 6px rgba(0,0,0,.15);color:var(--white);font-family:"Raleway",sans-serif;font-weight:600;font-size:16px;display:flex;align-items:center;justify-content:center;z-index:1}
.service-art{height:220px;width:300px;border-radius:6px}
.service-left.service-art{left:220px}
.art-cloud{background:linear-gradient(160deg,#dcdcdc,#c7c7c7)}
.art-consult{background:linear-gradient(160deg,#d8d8d8,#c4c4c4)}
.art-care{background:linear-gradient(160deg,#f0d9c4,#e3c0a5)}

/* tabs */
.tabs{height:130px;background:var(--charcoal);display:flex;justify-content:center}
.tab{width:340px;display:flex;align-items:center;justify-content:center;border-right:1px solid #4b4b4d}
.tab:last-child{border-right:0}
.tab.active{background:var(--blue)}

/* cloud feature */
.feature{height:440px;background:var(--blue);display:flex;align-items:center;padding:0 90px;gap:70px;color:var(--white)}
.feature-visual{width:420px;height:260px;flex-shrink:0;border-radius:130px;background:linear-gradient(180deg,var(--blue-soft),rgba(95,191,233,.6));display:flex;align-items:center;padding-left:70px}
.feature-visual span{font-family:"Raleway",sans-serif;font-size:46px;font-weight:600}
.feature-copy h2{font-size:30px;font-weight:700;margin-bottom:14px}
.feature-copy p{font-size:13.5px;margin-bottom:14px;opacity:.95}
.btns{display:flex;gap:14px;margin-top:10px}
.btn{padding:10px 26px;font-size:13px;font-family:"Raleway",sans-serif;font-weight:600;text-decoration:none;border:2px solid var(--white)}
.btn-solid{background:var(--white);color:var(--blue)}
.btn-ghost{color:var(--white)}

/* clients */
.clients{height:450px;padding-top:50px}
.section-title{text-align:center;font-size:30px;font-weight:600;margin-bottom:36px;color:var(--ink)}
.client-grid{width:1040px;margin:0 auto;display:grid;grid-template-columns:repeat(6,1fr);grid-template-rows:150px 150px}
.tile{padding:16px;font-size:12px;color:var(--white);overflow:hidden}
.tile.photo-a{background:linear-gradient(135deg,#9fc7dd,#6fa6c6)}
.tile.photo-b{background:linear-gradient(135deg,#c9d3db,#98a9b6)}
.tile.photo-c{background:linear-gradient(135deg,#e8b795,#c98a64)}
.tile.photo-d{background:linear-gradient(135deg,#b8c6cf,#7f95a4)}
.tile.blue{background:var(--blue)}
.tile.orange{background:var(--orange)}
.tile.grey{background:#9c9c9c}

/* people */
.people{height:560px;background:var(--light);padding-top:50px;position:relative}
.people-row{display:flex;gap:24px;width:1000px;margin:0 auto}
.person{width:232px;background:var(--white);box-shadow:0 2px 8px rgba(0,0,0,.1);text-align:center;padding-bottom:20px}
.person-photo{height:200px;background:linear-gradient(160deg,#8fc3e2,#4c9cc9)}
.person-photo.warm{background:linear-gradient(160deg,#f5c48f,#e59a4e)}
.person h3{font-size:17px;font-weight:700;margin-top:16px}
.person .role{color:var(--orange);font-size:12px;font-weight:600}
.person p{font-size:12px;color:var(--muted);padding:8px 22px}
.socials{display:flex;justify-content:center;gap:8px;margin-top:6px}
.socials span{width:22px;height:22px;border-radius:50%;border:1.5px solid var(--blue)}
.arrow{position:absolute;top:300px}
.arrow.prev{left:40px}.arrow.next{right:40px}

/* contact */
.contact{height:700px;position:relative;padding-top:60px}
.map{position:absolute;inset:0;background:linear-gradient(135deg,#9a9a9a 0%,#c4c4c4 40%,#8d8d8d 100%)}
.contact .section-title{position:relative;color:var(--charcoal-dark);margin-bottom:24px}
.contact-panel{position:relative;width:960px;margin:0 auto;background:var(--orange);color:var(--white);padding:34px 40px;box-shadow:0 4px 14px rgba(0,0,0,.25)}
.offices{display:grid;grid-template-columns:repeat(3,1fr);gap:30px;margin-bottom:30px}
.office h4{font-size:14px;font-weight:700;margin-bottom:12px}
.office li{list-style:none;display:flex;gap:10px;font-size:12.5px;margin-bottom:10px;align-items:flex-start}
.office svg{flex-shrink:0;margin-top:3px}
.form-row{display:flex;gap:20px;margin-bottom:16px}
.field{flex:1;height:40px;background:var(--white);color:#9a9a9a;font-size:13px;padding:10px 14px}
.field.message{height:90px}
.form-foot{display:flex;gap:20px;align-items:flex-end}
.btn-dark{background:var(--charcoal);color:var(--white);padding:10px 26px;font-size:13px;font-family:"Raleway",sans-serif;font-weight:600;white-space:nowrap}

/* newsletter */
.newsletter{height:360px;padding-top:60px;text-align:center}
.newsletter h2{font-size:28px;font-weight:600;margin-bottom:34px}
.news-row{display:flex;align-items:center;justify-content:center;gap:24px}
.news-row p{width:260px;text-align:left;font-size:13px;color:var(--muted)}
.news-input{width:300px;height:42px;border:1px solid #cfcfcf;text-align:left;padding:10px 14px;color:#9a9a9a;font-size:13px}

/* footer */
.site-footer{height:420px;background:var(--charcoal);color:#c8c8c8;padding:50px 80px 0}
.footer-cols{display:grid;grid-template-columns:1fr 1fr 1.3fr 1fr;gap:40px}
.footer-cols h4{color:var(--white);font-size:14px;font-weight:700;margin-bottom:14px;letter-spacing:.5px}
.footer-cols li{list-style:none;font-size:12.5px;margin-bottom:6px}
.support-title{margin-top:20px}
.blog-item{display:flex;gap:10px;margin-bottom:14px}
.blog-thumb{width:54px;height:44px;background:linear-gradient(135deg,#6f6f72,#505052);flex-shrink:0}
.blog-item p{font-size:12px;color:var(--white)}
.blog-item span{font-size:11px;color:#9a9a9a}
.follow{display:grid;grid-template-columns:repeat(4,32px);gap:10px}
.follow span{width:32px;height:32px;border-radius:50%;background:#5a5a5d}
.footer-brand{margin-top:40px;font-family:"Raleway",sans-serif;font-weight:600;font-size:22px;color:var(--white)}
.copyright{height:60px;background:var(--charcoal-dark);color:#9a9a9a;font-size:12px;display:flex;align-items:center;justify-content:center}
</style>
</head>
<body>

<header class="site-header">
  <div class="brand">Kovrel Associates</div>
  <nav class="main-nav">
    <a href="#">Our Company</a><a href="#">What we do</a><a href="#">Our Clients</a><a href="#">Our People</a><a href="#">Events</a><a href="#">Blog</a><a href="#">Contact Us</a>
  </nav>
</header>

<section class="hero">
  <div class="hero-copy">
    <h1>Trusted PMO Partners</h1>
    <p>Smart Project Portfolio Managment Tools<br>powered by Veltrix</p>
  </div>
  <div class="hero-art ph" role="img" aria-label="Word cloud of project management terms surrounded by illustrated team members with headsets"></div>
</section>

<section class="intro">
  <p><strong>Kovrel Associates</strong> is a specialist consulting company that focuses solely on the design, configuration, deployment, user training and support of <strong>Enterprise Portfolio Delivery (EPD)</strong> projects based upon <strong>Veltrix Project Server</strong> and its <strong>supporting technologies</strong>. <strong>Kovrel Associates</strong> is a single source for end-to-end service, from discovery through rollout to the lifecycle of the platform.</p>
  <p>This tight focus on Veltrix EPD solutions means that the company has an in-depth knowledge and experience that is unique in the local marketplace. Whether it is a complete implementation project, a hosted solution option or an ongoing support arrangement, <strong>Kovrel Associates</strong> has the services to meet its customers' needs.</p>
  <p>The team come from a diverse range of backgrounds including Engineering, Civil, Chemical and Systems, Project Management and Software Development. A number have worked with Veltrix and Veltrix Consulting Services directly. <strong>Kovrel Associates</strong> continues to work closely with Veltrix to ensure awareness of latest product developments.</p>
</section>

<section class="services">
  <div class="service">
    <p class="service-left service-text">Lorem ipsum is simply dummy text of the printing and typesetting industry. Lorem Ipsum has been the industry's standard dummy text ever since the 1500s, when an unknown printer took a galley of type and scrambled it to make a type specimen book. It has survived not only five centuries, but also the leap into electronic typesetting, remaining essentially unchanged.</p>
    <div class="service-node">Cloud</div>
    <div class="service-right service-art art-cloud ph" role="img" aria-label="Cloud platform illustration with project online window and connected devices"></div>
  </div>
  <div class="service">
    <div class="service-left service-art art-consult ph" role="img" aria-label="Consultant at a whiteboard presenting charts"></div>
    <div class="service-node">Consult</div>
    <p class="service-right service-text">Lorem ipsum is simply dummy text of the printing and typesetting industry. Lorem Ipsum has been the industry's standard dummy text ever since the 1500s, when an unknown printer took a galley of type and scrambled it to make a type specimen book. It has survived not only five centuries, but also the leap into electronic typesetting, remaining essentially unchanged.</p>
  </div>
  <div class="service">
    <p class="service-left service-text">Lorem ipsum is simply dummy text of the printing and typesetting industry. Lorem Ipsum has been the industry's standard dummy text ever since the 1500s, when an unknown printer took a galley of type and scrambled it to make a type specimen book. It has survived not only five centuries, but also the leap into electronic typesetting, remaining essentially unchanged.</p>
    <div class="service-node">Care</div>
    <div class="service-right service-art art-care ph" role="img" aria-label="Support agent with headset working at a desk"></div>
  </div>
</section>

<nav class="tabs">
  <div class="tab active">
    <svg width="90" height="60" viewBox="0 0 90 60" aria-hidden="true"><path d="M22 52h48a16 16 0 0 0 0-32 22 22 0 0 0-42-4 18 18 0 0 0-6 36z" fill="none" stroke="#fff" stroke-width="3"/></svg>
  </div>
  <div class="tab">
    <svg width="70" height="60" viewBox="0 0 70 60" aria-hidden="true"><path d="M35 6c17 0 30 10 30 22S52 50 35 50c-4 0-8-.6-11-1.7L10 55l4-11C8 39 5 34 5 28 5 16 18 6 35 6z" fill="none" stroke="#fff" stroke-width="3"/></svg>
  </div>
  <div class="tab">
    <svg width="70" height="60" viewBox="0 0 70 60" aria-hidden="true"><g stroke="#f7931e" stroke-width="6" stroke-linecap="round"><line x1="14" y1="50" x2="52" y2="12"/><line x1="16" y1="12" x2="54" y2="50"/></g></svg>
  </div>
</nav>

<section class="feature">
  <div class="feature-visual" role="img" aria-label="Large pale cloud illustration behind the service name"><span>Cloud</span></div>
  <div class="feature-copy">
    <h2>Fully customizable, fully flexable</h2>
    <p>Lorem general dual cloud solution provides a flexible private cloud solution tailored to your security, availability and extensibility requirements.</p>
    <p>Start with a single dedicated application server and leverage the availability and performance of our shared SQL tier, and build your own fully scalable private solution with our dedicated SQL options, or have dedicated servers for application, web and SQL.</p>
    <div class="btns"><a class="btn btn-solid" href="#">Get in Now</a><a class="btn btn-ghost" href="#">Learn More</a></div>
  </div>
</section>

<section class="clients">
  <h2 class="section-title">Our Clients</h2>
  <div class="client-grid">
    <div class="tile photo-a ph" role="img" aria-label="Team meeting around a laptop"></div>
    <div class="tile orange">Lorem ipsum is simply dummy text of the printing.</div>
    <div class="tile photo-b ph" role="img" aria-label="Office workers at desks"></div>
    <div class="tile photo-d ph" role="img" aria-label="Business presentation"></div>
    <div class="tile grey">Lorem ipsum is simply dummy text of the printing and typesetting industry. Lorem ipsum they developed with keyboards.</div>
    <div class="tile photo-c ph" role="img" aria-label="Hand-drawn user benefits notes"></div>
    <div class="tile blue">Lorem ipsum dummy text of the printing industry.</div>
    <div class="tile photo-b ph" role="img" aria-label="Colleagues collaborating"></div>
    <div class="tile photo-a ph" role="img" aria-label="Workshop with sticky notes"></div>
    <div class="tile orange">Lorem ipsum is simply dummy text of the typesetting.</div>
    <div class="tile photo-d ph" role="img" aria-label="Tablet showing dashboard"></div>
    <div class="tile blue">Lorem ipsum is simply dummy text of the printing.</div>
  </div>
</section>

<section class="people">
  <h2 class="section-title">Meet our People</h2>
  <svg class="arrow prev" width="30" height="30" viewBox="0 0 30 30" aria-hidden="true"><path d="M19 5 9 15l10 10" fill="none" stroke="#999" stroke-width="3"/></svg>
  <div class="people-row">
    <article class="person"><div class="person-photo ph" role="img" aria-label="Portrait of team member"></div><h3>John Smith</h3><div class="role">President CEO</div><p>Lorem ipsum is simply dummy text of the printing and type setting industry.</p><div class="socials"><span></span><span></span><span></span></div></article>
    <article class="person"><div class="person-photo warm ph" role="img" aria-label="Portrait of team member"></div><h3>John Smith</h3><div class="role">President CEO</div><p>Lorem ipsum is simply dummy text of the printing and type setting industry.</p><div class="socials"><span></span><span></span><span></span></div></article>
    <article class="person"><div class="person-photo warm ph" role="img" aria-label="Portrait of team member"></div><h3>John Smith</h3><div class="role">President CEO</div><p>Lorem ipsum is simply dummy text of the printing and type setting industry.</p><div class="socials"><span></span><span></span><span></span></div></article>
    <article class="person"><div class="person-photo ph" role="img" aria-label="Portrait of team member"></div><h3>John Smith</h3><div class="role">President CEO</div><p>Lorem ipsum is simply dummy text of the printing and type setting industry.</p><div class="socials"><span></span><span></span><span></span></div></article>
  </div>
  <svg class="arrow next" width="30" height="30" viewBox="0 0 30 30" aria-hidden="true"><path d="m11 5 10 10-10 10" fill="none" stroke="#999" stroke-width="3"/></svg>
</section>

<section class="contact">
  <div class="map ph" role="img" aria-label="Greyscale aerial city map background"></div>
  <h2 class="section-title">Contact Us</h2>
  <div class="contact-panel">
    <div class="offices">
      <div class="office">
        <h4>Kovrel Associates Head Office</h4>
        <ul>
          <li><svg width="12" height="14" viewBox="0 0 12 14"><path d="M6 0a5 5 0 0 1 5 5c0 4-5 9-5 9S1 9 1 5a5 5 0 0 1 5-5z" fill="#fff"/></svg>Suite 104, Level 6, 22 Marlow Street, Harlow Bay 4120</li>
          <li><svg width="12" height="12" viewBox="0 0 12 12"><path d="M2 0h3l1 3-2 1a7 7 0 0 0 4 4l1-2 3 1v3c0 1-1 2-2 2C5 12 0 7 0 2c0-1 1-2 2-2z" fill="#fff"/></svg>(04) 5521 8830</li>
          <li><svg width="12" height="12" viewBox="0 0 12 12"><rect x="1" y="3" width="10" height="8" fill="#fff"/></svg>(04) 5521 8831</li>
        </ul>
      </div>
      <div class="office">
        <h4>Kovrel Associates North Office</h4>
        <ul>
          <li><svg width="12" height="14" viewBox="0 0 12 14"><path d="M6 0a5 5 0 0 1 5 5c0 4-5 9-5 9S1 9 1 5a5 5 0 0 1 5-5z" fill="#fff"/></svg>Level 3, 18 Fenwick Lane, Arden Vale 3308</li>
          <li><svg width="12" height="12" viewBox="0 0 12 12"><path d="M2 0h3l1 3-2 1a7 7 0 0 0 4 4l1-2 3 1v3c0 1-1 2-2 2C5 12 0 7 0 2c0-1 1-2 2-2z" fill="#fff"/></svg>(03) 6610 2274</li>
          <li><svg width="12" height="12" viewBox="0 0 12 12"><rect x="1" y="3" width="10" height="8" fill="#fff"/></svg>(03) 6610 2275</li>
        </ul>
      </div>
      <div class="office">
        <h4>Kovrel Associates Capital Office</h4>
        <ul>
          <li><svg width="12" height="14" viewBox="0 0 12 14"><path d="M6 0a5 5 0 0 1 5 5c0 4-5 9-5 9S1 9 1 5a5 5 0 0 1 5-5z" fill="#fff"/></svg>Tower 2, Level 5, 9 Corran Place, Brellin 2910</li>
          <li><svg width="12" height="12" viewBox="0 0 12 12"><path d="M2 0h3l1 3-2 1a7 7 0 0 0 4 4l1-2 3 1v3c0 1-1 2-2 2C5 12 0 7 0 2c0-1 1-2 2-2z" fill="#fff"/></svg>(02) 7340 1196</li>
          <li><svg width="12" height="12" viewBox="0 0 12 12"><rect x="1" y="3" width="10" height="8" fill="#fff"/></svg>(02) 7340 1197</li>
        </ul>
      </div>
    </div>
    <div class="form-row"><div class="field">Name</div><div class="field">Email</div></div>
    <div class="form-foot"><div class="field message">Message</div><div class="btn-dark">Contact us</div></div>
  </div>
</section>

<section class="newsletter">
  <h2>Subscribe to our Newsletter</h2>
  <div class="news-row">
    <svg width="80" height="60" viewBox="0 0 80 60" aria-hidden="true"><rect x="4" y="8" width="72" height="48" fill="#29a9e1"/><path d="M4 8l36 28 36-28" fill="none" stroke="#fff" stroke-width="3"/></svg>
    <p>Lorem ipsum is simply dummy text of the printing and type setting industry.</p>
    <div class="news-input">Your email</div>
    <div class="btn-dark">Subscribe</div>
  </div>
</section>

<footer class="site-footer">
  <div class="footer-cols">
    <div><h4>ABOUT US</h4><ul><li>About</li><li>Industry Recognition</li><li>Partners</li><li>Team Members</li></ul>
      <div class="footer-brand">Kovrel Associates</div></div>
    <div><h4>CONTACT US</h4><ul><li>Harlow Bay 4120</li><li>(04) 5521 8830</li><li>22 Marlow Street</li><li>Level 6, Suite 104</li></ul>
      <h4 class="support-title">SUPPORT</h4><ul><li>Contact Support</li></ul></div>
    <div><h4>LATEST BLOG</h4>
      <div class="blog-item"><div class="blog-thumb ph" role="img" aria-label="Blog thumbnail"></div><div><p>Lorem ipsum is simply dummy text of the printing</p><span>12 March 2015</span></div></div>
      <div class="blog-item"><div class="blog-thumb ph" role="img" aria-label="Blog thumbnail"></div><div><p>Lorem ipsum is simply dummy text of the printing</p><span>04 March 2015</span></div></div>
      <div class="blog-item"><div class="blog-thumb ph" role="img" aria-label="Blog thumbnail"></div><div><p>Lorem ipsum is simply dummy text of the printing</p><span>27 February 2015</span></div></div>
    </div>
    <div><h4>FOLLOW US</h4><div class="follow"><span></span><span></span><span></span><span></span><span></span><span></span><span></span><span></span></div></div>
  </div>
</footer>
<div class="copyright">Copyright © 2015 Kovrel Associates. All Rights Reserved. Terms &amp; Conditions</div>

</body>
</html>
```